Quill Scholars Homepage and Landing Page Redesign

Quill Scholars 789 is a premier test preparation, academic consultation, and private tutoring company based in Los Angeles. We offer our tutoring in-person and also online. <br/><br/>We will need three mockups that are as follows:<br/><br/>1. A mockup of a homepage that will be on www.quillscholars789.com<br/>2. A mockup of a free-standing true landing page that will be a one-page site where we will direct traffic from a Google PPC ad.<br/>3. A mockup of a landing page that will replace a landing page such as the one at www.quillscholars789.com/test-prep-services/k-12/sat/ <br/><br/>Please see the word attached for details.

Target Market(s)

Middle School and High School Student Parents, College Students.

Industry/Entity Type

Tutoring

Number of Pages Required

3 page

Colors

Designer to choose colors to be used in the design.

Requirements
Must have
• The design of these 3 pages will need to fit within the overall design of the main website. We're looking for a user-friendly, easy-to-navigate, yet professional design.

```html
<!DOCTYPE html>
<html lang="en">
<head>
<meta charset="utf-8">
<title>Quill Scholars – Home</title>
<link href="https://fonts.googleapis.com/css2?family=Montserrat:wght@500;600;700;800&family=Open+Sans:ital,wght@0,400;0,600;0,700;1,400&display=swap" rel="stylesheet">
<style>
:root{
  --teal:#1f7c84;
  --teal-dark:#17656c;
  --teal-soft:#2aa6a2;
  --yellow:#f6c61a;
  --blue:#3ab0e2;
  --orange:#e8643a;
  --pink:#f2b5b0;
  --ink:#1d2a33;
  --grey:#6d7880;
  --line:#d9dfe3;
  --white:#ffffff;
}
*{box-sizing:border-box;margin:0;padding:0}
html,body{width:1200px;height:4416px;overflow:hidden}
body{font-family:"Open Sans",sans-serif;color:var(--ink);background:var(--white);position:relative}
.abs{position:absolute}
h1,h2,h3,h4{font-family:"Montserrat",sans-serif;font-weight:800;text-transform:uppercase;letter-spacing:.5px}
.placeholder{position:absolute}

/* header */
.site-header{position:absolute;top:0;left:0;width:1200px;height:72px;background:var(--white);display:flex;align-items:center;justify-content:space-between;padding:0 40px 0 72px;box-shadow:0 2px 6px rgba(0,0,0,.06);z-index:2}
.brand{display:flex;align-items:center;gap:10px;font-family:"Montserrat",sans-serif;font-weight:800;font-size:22px;color:var(--teal)}
.brand-mark{width:14px;height:14px;background:var(--yellow)}
.main-nav{display:flex;gap:30px;font-family:"Montserrat",sans-serif;font-weight:600;font-size:12px;letter-spacing:1px;color:var(--grey)}
.main-nav .active{background:var(--yellow);color:var(--ink);padding:6px 12px;margin:-6px 0}

/* hero */
.hero{position:absolute;top:72px;left:0;width:1200px;height:548px;background:linear-gradient(90deg,#f1efe9 0%,#eef4f4 55%,#e3f0f0 100%)}
.hero-photo{left:0;top:0;width:660px;height:548px;background:linear-gradient(120deg,#d8cbb8,#b9a48c 55%,#eae4da)}
.hero-copy{right:60px;top:150px;text-align:right;width:460px}
.hero-copy h1{font-size:42px;line-height:1.15;color:var(--ink)}
.hero-copy p{font-size:15px;font-style:italic;color:var(--grey);margin:18px 0 28px;line-height:1.6}
.btn{display:inline-block;background:var(--yellow);color:var(--ink);font-family:"Montserrat",sans-serif;font-weight:700;font-size:13px;letter-spacing:1px;padding:14px 30px;border-radius:30px;text-transform:uppercase}

/* test prep */
.section-title{font-size:38px;color:var(--ink)}
.test-prep-title{left:80px;top:712px}
.service{width:240px}
.service .icon{width:44px;height:44px;border-radius:4px;margin-bottom:14px;display:flex;align-items:center;justify-content:center}
.service h4{font-size:14px;margin-bottom:10px}
.service p{font-size:13px;line-height:1.6;color:var(--grey)}
.grad-photo{left:700px;top:690px;width:480px;height:680px;border-radius:48% 52% 42% 58%/40% 38% 62% 60%;background:linear-gradient(160deg,#cfd6da,#8e9ba3 60%,#3b3f44)}

/* stats */
.stat{display:flex;flex-direction:column;align-items:center;justify-content:center;text-align:center;color:var(--white);padding:0 40px}
.stat .label{font-family:"Montserrat",sans-serif;font-weight:800;font-size:30px}
.stat .num{font-family:"Montserrat",sans-serif;font-weight:800;font-size:60px;line-height:1}
.stat .note{font-size:12px;font-style:italic;margin-top:10px;line-height:1.4}
.stat-blue{left:70px;top:1370px;width:320px;height:350px;background:var(--blue);border-radius:55% 45% 50% 50%/50% 55% 45% 50%}
.stat-yellow{left:385px;top:1440px;width:270px;height:320px;background:var(--yellow);border-radius:50% 50% 45% 55%/55% 45% 55% 45%;color:var(--ink)}
.stat-orange{left:80px;top:1680px;width:270px;height:330px;background:var(--orange);border-radius:45% 55% 55% 45%/50% 50% 50% 50%}
.stat-teal{left:360px;top:1700px;width:290px;height:350px;background:var(--teal-soft);border-radius:55% 45% 50% 50%/45% 55% 50% 50%}
.results{left:680px;top:1610px;width:460px}
.results h2{font-size:30px;line-height:1.25;margin-bottom:20px}
.results p{font-size:14px;font-style:italic;color:var(--grey);line-height:1.7}

/* steps */
.steps-title{top:2160px;left:0;width:1200px;text-align:center;font-size:34px}
.steps-line{left:320px;top:2292px;width:560px;height:2px;background:var(--line)}
.step{width:220px;text-align:center;top:2255px}
.step .dot{width:76px;height:76px;border-radius:50%;margin:0 auto 16px;display:flex;align-items:center;justify-content:center;font-family:"Montserrat",sans-serif;font-weight:800;font-size:26px;background:var(--yellow);border:6px solid #fff;box-shadow:0 0 0 2px var(--line)}
.step .dot.current{background:var(--teal);color:#fff}
.step p{font-size:13px;font-weight:600;line-height:1.4}
.step p.current{color:var(--teal)}

/* match */
.match-photo{left:150px;top:2420px;width:420px;height:340px;border-radius:40% 60% 50% 50%/50% 40% 60% 50%;background:linear-gradient(120deg,#c9b9a4,#8d7b68 55%,#d7d3cd)}
.match-copy{left:610px;top:2520px;width:520px}
.match-copy h3{font-size:20px;text-transform:none;color:var(--teal);margin-bottom:14px;font-weight:700}
.match-copy p{font-size:14px;color:var(--grey);line-height:1.7}

/* tutors */
.tutors-title{top:2830px;left:0;width:1200px;text-align:center;font-size:40px;line-height:1.2}
.tutor{top:2950px;width:240px;text-align:center}
.tutor .photo{width:210px;height:210px;border-radius:50% 50% 46% 54%/52% 48% 52% 48%;margin:0 auto 20px}
.tutor h4{font-size:17px}
.tutor .spec{font-size:13px;color:var(--teal);font-weight:700;margin:6px 0 8px}
.tutor .school{font-size:12px;color:var(--grey);line-height:1.5}

/* consultation */
.teal-band{left:0;top:3440px;width:1200px;height:976px;background:var(--teal)}
.consult-card{left:230px;top:3360px;width:740px;height:600px;background:#fff;border-radius:0 0 60px 60px;text-align:center;padding-top:90px}
.consult-card h2{font-size:34px}
.consult-card .intro{font-size:14px;font-style:italic;color:var(--grey);margin:16px auto 40px;width:520px;line-height:1.6}
.form{display:grid;grid-template-columns:250px 250px;gap:24px 30px;justify-content:center}
.field{border:1px solid var(--line);border-radius:4px;height:42px;font-size:13px;color:var(--grey);text-align:left;padding:11px 14px}
.form .btn{grid-column:1/3;justify-self:center;margin-top:10px}

/* footer */
.footer-brand{left:80px;top:4050px;width:300px}
.footer-brand .brand{color:#fff;font-size:24px;margin-bottom:18px}
.footer-brand p{font-size:13px;color:#e3f0f0;line-height:1.6;margin-bottom:10px}
.footer-col{top:4060px;width:210px;color:#e3f0f0;font-size:13px}
.footer-col h4{color:var(--yellow);font-size:13px;letter-spacing:1px;margin-bottom:16px}
.footer-col li{list-style:none;margin-bottom:6px}
.footer-col li::before{content:"› ";color:var(--yellow)}
.contact-line{display:flex;gap:10px;align-items:flex-start;margin-bottom:12px;line-height:1.5}
.footer-bottom{left:0;top:4340px;width:1200px;border-top:1px solid rgba(255,255,255,.2);padding-top:24px;text-align:center;font-size:11px;color:#cfe3e3}
</style>
</head>
<body>

<header class="site-header">
  <div class="brand"><span class="brand-mark"></span>Quill Scholars</div>
  <nav class="main-nav">
    <span class="active">HOME</span><span>ACADEMIC SUPPORT</span><span>TEST PREP</span><span>ABOUT</span><span>RESOURCES</span><span>CONTACT</span>
  </nav>
</header>

<section class="hero">
  <div class="placeholder hero-photo" role="img" aria-label="Photo of two smiling students studying together at a laptop"></div>
  <div class="abs hero-copy">
    <h1>We provide the<br>best tutors</h1>
    <p>Experienced, professional tutors available for private sessions either in-home in Los Angeles or online, worldwide.</p>
    <span class="btn">Free Consultation</span>
  </div>
</section>

<h2 class="abs section-title test-prep-title">Test Prep</h2>
<div class="abs service" style="left:80px;top:790px">
  <div class="icon" style="background:var(--blue)"><svg width="24" height="24" viewBox="0 0 24 24" fill="none" stroke="#fff" stroke-width="2"><path d="M4 5h10v14H4zM14 8h6v11h-6"/></svg></div>
  <h4>Academic Tutoring</h4>
  <p>Work with one of our expert tutors to supplement what you’re learning in school. We will help you stay on track or make gains as you go.</p>
</div>
<div class="abs service" style="left:360px;top:790px">
  <div class="icon" style="background:var(--yellow)"><svg width="24" height="24" viewBox="0 0 24 24" fill="none" stroke="#fff" stroke-width="2"><path d="M6 4h12v16H6zM9 9h6M9 13h6"/></svg></div>
  <h4>K-12 / College Test Prep</h4>
  <p>Work one-on-one with one of our veteran tutors to help you achieve your test prep goals: SAT, ACT, SSAT, ISEE, HSPT and more.</p>
</div>
<div class="abs service" style="left:80px;top:1010px">
  <div class="icon" style="background:var(--orange)"><svg width="24" height="24" viewBox="0 0 24 24" fill="none" stroke="#fff" stroke-width="2"><path d="M3 10l9-5 9 5-9 5z M7 12v5h10v-5"/></svg></div>
  <h4>Graduate Test Prep</h4>
  <p>Prepare for your graduate-level exam with one of our experienced tutors and customize your learning plan: GMAT, GRE.</p>
</div>
<div class="abs service" style="left:360px;top:1010px">
  <div class="icon" style="background:var(--teal-soft)"><svg width="24" height="24" viewBox="0 0 24 24" fill="none" stroke="#fff" stroke-width="2"><circle cx="12" cy="12" r="8"/><path d="M8 12l3 3 5-6"/></svg></div>
  <h4>Professional Test Prep</h4>
  <p>Connect with a specialist who can work around your schedule and help you pass your professional test: CBEST, CSET, TOEFL.</p>
</div>
<div class="placeholder grad-photo" role="img" aria-label="Photo of a smiling graduate in cap and gown holding a diploma"></div>

<div class="abs stat stat-blue"><span class="label">SAT</span><span class="num">150</span><span class="note">Our students average a 150 point increase on the SAT</span></div>
<div class="abs stat stat-yellow"><span class="label">SAT</span><span class="num">2.5</span><span class="note">Our students average a 2.5 increase on the SAT essay</span></div>
<div class="abs stat stat-orange"><span class="label">ACT</span><span class="num">4</span><span class="note">Our students average a 4 point increase on the ACT</span></div>
<div class="abs stat stat-teal"><span class="label">CSET</span><span class="num">90%</span><span class="note">Over 90% of our students pass the CSET</span></div>
<div class="abs results">
  <h2>Proven results from a tutoring company you can trust</h2>
  <p>Quill Scholars only works with highly experienced, professional, veteran tutors who have a proven track record of success. Our individualized approach has helped countless students achieve the academic and test prep goals of their dreams.</p>
</div>

<h2 class="abs section-title steps-title">It’s as easy as 1-2-3</h2>
<div class="abs steps-line"></div>
<div class="abs step" style="left:210px"><div class="dot">1</div><p>Answer a Few Questions<br>About Your Needs</p></div>
<div class="abs step" style="left:490px"><div class="dot current">2</div><p class="current">We Match You With the<br>Perfect Tutor</p></div>
<div class="abs step" style="left:770px"><div class="dot">3</div><p>Schedule Your First<br>Session</p></div>

<div class="placeholder match-photo" role="img" aria-label="Photo of a tutor and student working together at a laptop"></div>
<div class="abs match-copy">
  <h3>We Match You With the Perfect Tutor</h3>
  <p>One of the most crucial parts of working with a tutor is ensuring that it’s a right fit. Once we understand which type of tutor personality will work best for you, we reach out to our tutors to confirm their availability and connect you to get started.</p>
</div>

<h2 class="abs section-title tutors-title">Meet some of<br>our experienced tutors</h2>
<div class="abs tutor" style="left:60px"><div class="photo" role="img" aria-label="Portrait of tutor Owen P." style="background:linear-gradient(160deg,#8fd3f0,var(--blue))"></div><h4>Owen P.</h4><p class="spec">Specializes in ISEE</p><p class="school">Calverton Institute of<br>Technology Ph.D. candidate</p></div>
<div class="abs tutor" style="left:340px"><div class="photo" role="img" aria-label="Portrait of tutor Maya K." style="background:linear-gradient(160deg,#fbe08a,var(--yellow))"></div><h4>Maya K.</h4><p class="spec">Specializes in ACT</p><p class="school">Dunmere College B.E. in<br>Mechanical Engineering</p></div>
<div class="abs tutor" style="left:620px"><div class="photo" role="img" aria-label="Portrait of tutor Julian R." style="background:linear-gradient(160deg,#c9e8f3,#9fd2e6)"></div><h4>Julian R.</h4><p class="spec">Specializes in HSPT</p><p class="school">Harwick Vale University<br>B.A. in Literature</p></div>
<div class="abs tutor" style="left:890px"><div class="photo" role="img" aria-label="Portrait of tutor Elena S." style="background:linear-gradient(160deg,#f8d3cf,var(--pink))"></div><h4>Elena S.</h4><p class="spec">Specializes in SAT</p><p class="school">Pellingham University<br>B.A. in Politics</p></div>

<div class="abs teal-band"></div>
<section class="abs consult-card">
  <h2>Free Consultation</h2>
  <p class="intro">Our elite team of tutors has been helping students realize their academic potential for over a decade. Let us do the same for you.</p>
  <div class="form">
    <div class="field">Name*</div><div class="field">Email*</div>
    <div class="field">Phone*</div><div class="field">Zipcode*</div>
    <div class="field">School Name</div><div></div>
    <span class="btn">Send Email</span>
  </div>
</section>

<footer>
  <div class="abs footer-brand">
    <div class="brand"><span class="brand-mark"></span>Quill Scholars</div>
    <p>Quill Scholars 789 is a premier test preparation, academic consultation, and private tutoring company in Los Angeles.</p>
    <p>We specialize in SAT, ACT, ISEE, HSPT, GRE, CHSPE, GMAT, CBEST, and CSET. <span style="color:var(--yellow);font-weight:700">READ MORE</span></p>
  </div>
  <div class="abs footer-col" style="left:420px"><h4>OUR SERVICES</h4><ul><li>SAT</li><li>ACT</li><li>ISEE</li><li>CHSPE</li><li>GMAT</li><li>CSET</li></ul></div>
  <div class="abs footer-col" style="left:640px"><h4>MORE INFO</h4><ul><li>Tutoring Resources</li><li>FAQ</li><li>Blog</li><li>Tutoring Jobs</li><li>Innovation Scholarship</li><li>Free Diagnostic Test</li><li>Subscribe</li></ul></div>
  <div class="abs footer-col" style="left:880px;width:260px"><h4>GET IN TOUCH</h4>
    <div class="contact-line"><svg width="14" height="14" viewBox="0 0 24 24" fill="var(--yellow)"><path d="M12 2a7 7 0 0 0-7 7c0 5 7 13 7 13s7-8 7-13a7 7 0 0 0-7-7zm0 9.5A2.5 2.5 0 1 1 12 6.5a2.5 2.5 0 0 1 0 5z"/></svg><span>4120 Harbor Lane, Suite 300<br>Westwood, CA 90024</span></div>
    <div class="contact-line"><svg width="14" height="14" viewBox="0 0 24 24" fill="var(--yellow)"><path d="M6.6 10.8a15 15 0 0 0 6.6 6.6l2.2-2.2a1 1 0 0 1 1-.25 11.4 11.4 0 0 0 3.6.6 1 1 0 0 1 1 1V20a1 1 0 0 1-1 1A17 17 0 0 1 3 4a1 1 0 0 1 1-1h3.5a1 1 0 0 1 1 1 11.4 11.4 0 0 0 .6 3.6 1 1 0 0 1-.25 1z"/></svg><span>310-555-0148</span></div>
    <div class="contact-line"><svg width="14" height="14" viewBox="0 0 24 24" fill="var(--yellow)"><path d="M3 5h18v14H3zm2 2v.5l7 5 7-5V7l-7 5z"/></svg><span style="font-weight:700">contact@quillscholars789.com</span></div>
  </div>
  <div class="abs footer-bottom">© 2021 Quill Scholars 789 – All Rights Reserved. &nbsp;|&nbsp; Privacy &amp; Terms of Use</div>
</footer>

</body>
</html>
```